New Church Plant website for Brightvale Church

I would like a six page website designed that is clean and easy to navigate. The six pages will include (1) About Us (2) Home (3) Contact Us (4) Sermons (5) Donate (6) Ministries. There will be subcategories for each category as well. The color scheme can be found in the attached magazine of Brightvale. Much of the information found in the booklet will be used on the website. I would love to see a design that pops but still clean and easy to navigate. I have included a good deal of pictures for the creative. Please see the current website at brightvalechapel.example which is temporary as we are preparing for a launch. I would now like to create a long-term site.

Target Market(s)

People interested in Christian church

Number of Pages Required

5+ page

Font styles to use
Sans Serif

Colors
ffffff
f78f20

Requirements
Must have
• a site that pops but is clean and easy to navigate.

```html
<!DOCTYPE html>
<html lang="en">
<head>
<meta charset="utf-8">
<title>Brightvale Church – About</title>
<link rel="stylesheet" href="https://fonts.googleapis.com/css2?family=Poppins:ital,wght@0,400;0,600;0,700;1,400&family=Lato:wght@300;400;700&display=swap">
<style>
:root{
  --orange:#f78f20;
  --white:#ffffff;
  --purple:#5a3d8f;
  --purple-dark:#3f2a6e;
  --ink:#444448;
  --muted:#7a7a7e;
  --ghost:#dedede;
  --dark:#2f2826;
}
*{margin:0;padding:0;box-sizing:border-box}
html,body{width:1070px;height:1200px;overflow:hidden;background:var(--white)}
body{position:relative;font-family:'Lato',sans-serif;color:var(--ink)}

.donate-band{position:absolute;left:0;top:0;width:1070px;height:49px;background:linear-gradient(90deg,var(--purple-dark),var(--purple) 60%,#6a4aa0)}
.donate-link{position:absolute;left:189px;top:6px;font-family:'Poppins',sans-serif;font-weight:600;font-size:15px;color:var(--white);border-bottom:1px solid var(--white);padding-bottom:1px}
.donate-arrow{position:absolute;left:260px;top:9px}
.card-badges{position:absolute;left:310px;top:9px;display:flex;gap:4px}
.card-badges span{width:23px;height:13px;background:var(--white);border-radius:1px}
.band-photo{position:absolute;left:696px;top:0;width:170px;height:49px;background:linear-gradient(180deg,#4d5a78,#6a7898)}

.portrait-frame{position:absolute;left:241px;top:131px;width:208px;height:366px;border:1.5px solid var(--orange)}
.portrait{position:absolute;left:213px;top:159px;width:206px;height:307px;background:radial-gradient(ellipse at 50% 35%,#6a3a28,#3a2218 70%),#3a2218}
.portrait::after{content:"";position:absolute;left:0;right:0;bottom:0;height:45%;background:linear-gradient(180deg,#d65a2c,#c24a22)}
.portrait-inner{position:absolute;left:225px;top:174px;width:183px;height:280px;border:1px solid rgba(255,255,255,.35);z-index:2}

.mission-title{position:absolute;left:212px;top:496px;font-family:'Poppins',sans-serif;font-weight:700;font-size:72px;letter-spacing:-1px;color:var(--ghost);line-height:1}
.mission-quote{position:absolute;left:213px;top:564px;width:270px;font-family:'Poppins',sans-serif;font-style:italic;font-size:14.5px;line-height:18.5px;color:#3a2a1a}
.mission-quote span{background:var(--orange);box-decoration-break:clone;-webkit-box-decoration-break:clone;padding:0 2px;border-radius:3px}

.bio{position:absolute;left:562px;top:182px;width:310px}
.bio-title{font-family:'Poppins',sans-serif;font-weight:600;font-size:28px;line-height:1;color:var(--ink)}
.bio-title strong{color:var(--orange);font-weight:700}
.bio-role{margin:4px 0 0 40px;font-size:15px;color:var(--muted)}
.bio p{font-weight:300;font-size:11.3px;line-height:18.3px;color:var(--muted);margin-top:16px}
.bio p + p{margin-top:18px}
.bio a{color:var(--orange);font-weight:400;text-decoration:none;margin-left:10px}
.edu-heading{font-family:'Poppins',sans-serif;font-weight:600;font-size:16px;color:var(--orange);margin-top:18px}
.edu-item{margin-top:10px}
.edu-item h3{font-size:12px;font-weight:700;color:var(--ink)}
.edu-item small{display:block;font-size:10px;color:var(--muted);margin-top:2px}

.values{position:absolute;left:0;top:695px;width:1070px;height:505px;background:linear-gradient(90deg,#2c2624 0%,#342c29 60%,#4a3a33 85%,#3a2f2b 100%)}
.values-title{position:absolute;left:0;width:1070px;top:90px;text-align:center;font-family:'Poppins',sans-serif;font-weight:700;font-size:28px;color:#8a8584}
.values-title strong{color:var(--orange)}
.value{position:absolute;display:flex;align-items:center;gap:14px;font-weight:700;font-size:14px;color:var(--white)}
.value svg{flex:none}
</style>
</head>
<body>

<header class="donate-band">
  <div class="band-photo" role="img" aria-label="Photo of the pastor standing, cropped at the legs"></div>
  <span class="donate-link">Donate</span>
  <svg class="donate-arrow" width="22" height="14" viewBox="0 0 22 14"><path d="M1 7h19M14 1l6 6-6 6" fill="none" stroke="#f78f20" stroke-width="2"/></svg>
  <div class="card-badges"><span></span><span></span><span></span><span></span><span></span></div>
</header>

<div class="portrait-frame"></div>
<div class="portrait" role="img" aria-label="Portrait of church planter Marcus Reed in an orange sweater"></div>
<div class="portrait-inner"></div>

<h2 class="mission-title">MISSION</h2>
<p class="mission-quote"><span>“To be a gospel centered, multi-ethnic, church planting church built on the pillars of missions, faith, work, and economics.”</span></p>

<section class="bio">
  <h1 class="bio-title">I am <strong>MARCUS</strong></h1>
  <div class="bio-role">church planter</div>
  <p>Marcus Reed was born and raise as preacher’s kid in the central city of Riverton. As a youth he was involved in gangs and by the age of 22, was a succcessful drug dealer.</p>
  <p>After a near death experience, he gave his life to jesus and later become an ordained minister. In 2005 he planted his first church in the city of Riverton. In 2016 he led the launch of a noth-side multi-ethnic ministry nitiative for Keystone church. <a href="#">Read My story here</a></p>
  <h2 class="edu-heading">Education</h2>
  <div class="edu-item"><h3>B.A in Business</h3><small>From Northfield University</small></div>
  <div class="edu-item"><h3>M.A. in Christian ministry</h3><small>From Harbor Ridge Theological Seminary</small></div>
  <div class="edu-item"><h3>E.d. D in Organizational Leadership (ABD)</h3><small>From Westmont Plains University</small></div>
</section>

<section class="values" role="img" aria-label="Dim photo of the pastor preaching on stage">
  <h2 class="values-title">Core <strong>Values</strong></h2>
  <div class="value" style="left:160px;top:173px"><svg width="40" height="38" viewBox="0 0 40 38"><path d="M2 22l6-5 8 9L36 2l3 4-22 31z" fill="#f78f20"/></svg>Bibilcal Centered Teachings</div>
  <div class="value" style="left:462px;top:173px"><svg width="40" height="38" viewBox="0 0 40 38"><path d="M2 22l6-5 8 9L36 2l3 4-22 31z" fill="#f78f20"/></svg>Diversity</div>
  <div class="value" style="left:692px;top:173px"><svg width="40" height="38" viewBox="0 0 40 38"><path d="M2 22l6-5 8 9L36 2l3 4-22 31z" fill="#f78f20"/></svg>Authencity</div>
  <div class="value" style="left:160px;top:248px"><svg width="40" height="38" viewBox="0 0 40 38"><path d="M2 22l6-5 8 9L36 2l3 4-22 31z" fill="#f78f20"/></svg>Vulnerability</div>
  <div class="value" style="left:462px;top:248px"><svg width="40" height="38" viewBox="0 0 40 38"><path d="M2 22l6-5 8 9L36 2l3 4-22 31z" fill="#f78f20"/></svg>Church Planting</div>
  <div class="value" style="left:692px;top:248px"><svg width="40" height="38" viewBox="0 0 40 38"><path d="M2 22l6-5 8 9L36 2l3 4-22 31z" fill="#f78f20"/></svg>The Unbeliveable</div>
  <div class="value" style="left:160px;top:324px"><svg width="40" height="38" viewBox="0 0 40 38"><path d="M2 22l6-5 8 9L36 2l3 4-22 31z" fill="#f78f20"/></svg>Local Missions</div>
  <div class="value" style="left:462px;top:324px"><svg width="40" height="38" viewBox="0 0 40 38"><path d="M2 22l6-5 8 9L36 2l3 4-22 31z" fill="#f78f20"/></svg>Human Flourishing</div>
  <div class="value" style="left:693px;top:324px"><svg width="40" height="38" viewBox="0 0 40 38"><path d="M2 22l6-5 8 9L36 2l3 4-22 31z" fill="#f78f20"/></svg>Life Groups &amp; Community</div>
  <div class="value" style="left:463px;top:399px"><svg width="40" height="38" viewBox="0 0 40 38"><path d="M2 22l6-5 8 9L36 2l3 4-22 31z" fill="#f78f20"/></svg>Unconditional Love</div>
</section>

</body>
</html>
```